Design a Door Hanger AD for a Pool Service Company

We're looking to design an ad for our Pool Service Company to hang on potential customers doors.

We would like to have one side showing a promotion stating that if they sign up with us for "Tervin Premium Pool Service" they'll get 60% off their first month of service (Regular price $100, after discount $40)
Service includes:
Weekly Pool Service
Water balance
Vacuum
Brush
Skim surface
Filter cleaning
Clean baskets
Salt Water Systems
All chemicals included
Algae prevention
Skimmer and Pump's basket replacement
Free Chlorine Tablet Dispenser

*** Tervin Monitoring Software *** (Highlight this service) With our software, customers can follow-up each visit. They'll receive updates to their email, pictures, and notifications every time we service their pools.

On the back side, we would like to show another promotion for current customers. They'll get $10 off if they refer us to a friend and sign up for "Tervin Premium Pool Service"

```html
<!DOCTYPE html>
<html lang="en">
<head>
<meta charset="utf-8">
<title>Tervin Pools Door Hanger</title>
<link href="https://fonts.googleapis.com/css2?family=Open+Sans:wght@400;600;700;800&family=Kaushan+Script&display=swap" rel="stylesheet">
<style>
  :root {
    --stage: #000000;
    --paper: #ffffff;
    --pool-deep: #0f6cbf;
    --pool: #1c8ed9;
    --pool-light: #4fb3ee;
    --splash: #aedcf7;
    --navy: #16385f;
    --ink: #1d2a38;
    --accent-blue: #1a6fc0;
  }
  * { box-sizing: border-box; margin: 0; padding: 0; }
  html, body { width: 1200px; height: 851px; overflow: hidden; background: var(--stage); }
  body { position: relative; font-family: "Open Sans", Arial, sans-serif; }

  .hanger {
    position: absolute; top: 11px; width: 343px; height: 831px;
    background: var(--paper); overflow: hidden;
  }
  .hanger--front { left: 151px; }
  .hanger--back { left: 700px; }

  .hanger__backdrop { position: absolute; inset: 0; width: 100%; height: 100%; }

  .hanger__hole {
    position: absolute; top: 1px; left: 114px; width: 114px; height: 114px;
    border-radius: 50%; background: var(--stage); z-index: 5;
  }

  .wave-art {
    position: absolute; border-radius: 40% 60% 30% 70%;
    background: radial-gradient(circle at 40% 40%, var(--pool-light), var(--pool-deep));
  }
  .splash-art {
    position: absolute; border-radius: 50%;
    background: radial-gradient(circle, var(--splash), rgba(174,220,247,0.2));
  }

  .offer-title {
    position: absolute; left: 0; right: 0; text-align: center;
    color: var(--paper); font-weight: 700; text-shadow: 0 2px 3px rgba(0,0,0,0.35);
  }
  .hanger--front .offer-title { top: 194px; font-size: 27px; line-height: 34px; letter-spacing: 0.3px; }
  .offer-detail {
    position: absolute; top: 282px; left: 0; right: 0; text-align: center;
    color: var(--paper); font-size: 13px; line-height: 18px; font-weight: 600;
  }

  .mascot-art {
    position: absolute; border-radius: 45%;
    background: radial-gradient(circle at 50% 40%, #6fc3ef, #2a78c2 70%, #1b5e9f);
  }
  .brand-name {
    position: absolute; color: var(--navy); font-weight: 800; text-align: center;
  }

  .service-list {
    position: absolute; top: 408px; left: 22px; list-style: none;
    color: var(--paper); font-size: 14.5px; line-height: 19.8px; font-weight: 600;
  }
  .service-list li { position: relative; padding-left: 13px; }
  .service-list li::before {
    content: ""; position: absolute; left: 0; top: 6px;
    border-left: 7px solid var(--paper); border-top: 4px solid transparent; border-bottom: 4px solid transparent;
  }

  .monitoring-box {
    position: absolute; left: 22px; top: 682px; width: 294px; height: 112px;
    background: var(--paper); box-shadow: 3px 4px 8px rgba(0,0,0,0.35);
    text-align: center; padding: 10px 10px 0;
  }
  .monitoring-box__title {
    font-family: "Kaushan Script", cursive; color: var(--accent-blue);
    font-size: 19px; line-height: 26px;
  }
  .monitoring-box__lead { font-size: 11px; line-height: 15px; color: var(--ink); margin-top: 6px; }
  .monitoring-box__note { font-size: 11px; line-height: 15px; color: var(--accent-blue); font-weight: 600; }

  .referral {
    position: absolute; top: 182px; left: 0; right: 0; text-align: center;
    color: var(--paper); font-size: 17px; line-height: 24px;
  }
  .referral__amount { font-size: 24px; font-weight: 700; line-height: 30px; }
  .referral__plan { font-weight: 700; font-size: 17px; }
</style>
</head>
<body>

<section class="hanger hanger--front" aria-label="Front side: new customer offer">
  <svg class="hanger__backdrop" viewBox="0 0 343 831" preserveAspectRatio="none" aria-hidden="true">
    <defs>
      <linearGradient id="poolFront" x1="0" y1="0" x2="0" y2="1">
        <stop offset="0" stop-color="#1f94dc"/>
        <stop offset="1" stop-color="#0f6cbf"/>
      </linearGradient>
    </defs>
    <path d="M0 160 C90 140 200 178 343 150 L343 831 L0 831 Z" fill="url(#poolFront)"/>
    <path d="M0 172 C110 150 220 188 343 162" fill="none" stroke="#ffffff" stroke-width="4" opacity="0.8"/>
    <path d="M0 360 C110 330 230 350 343 320 L343 520 C230 540 110 500 0 530 Z" fill="#2aa0e6" opacity="0.55"/>
  </svg>
  <div class="wave-art" style="left:4px;top:18px;width:130px;height:138px;" role="img" aria-label="Blue ocean wave illustration"></div>
  <div class="splash-art" style="left:226px;top:40px;width:110px;height:100px;" role="img" aria-label="Light blue water splash illustration"></div>
  <div class="hanger__hole"></div>

  <h1 class="offer-title">"TERVIN PREMIUM<br>POOL SERVICE"</h1>
  <p class="offer-detail">You'll get 60% off your first month of service<br>(Regular price $100, after discount $40)</p>

  <div class="mascot-art" style="left:140px;top:336px;width:186px;height:150px;" role="img" aria-label="Cartoon shark mascot holding a pool skimmer net"></div>
  <p class="brand-name" style="left:150px;top:476px;width:180px;font-size:26px;line-height:32px;color:#ffffff;">Tervin Pools</p>

  <ul class="service-list">
    <li>Weekly Pool Service</li>
    <li>Water balance</li>
    <li>Vacuum</li>
    <li>Brush</li>
    <li>Skim surface</li>
    <li>Filter cleaning</li>
    <li>Clean baskets</li>
    <li>Salt Water Systems</li>
    <li>All chemicals included</li>
    <li>Algae prevention</li>
    <li>Skimmer and Pump's basket<br>replacement</li>
    <li>Free Chlorine Tablet Dispenser</li>
  </ul>

  <div class="monitoring-box">
    <h2 class="monitoring-box__title">Tervin Monitoring Software</h2>
    <p class="monitoring-box__lead">With our software, customers can follow-up each visit.</p>
    <p class="monitoring-box__note">They'll receive updates to their email, pictures, and notifications every time we service their pools.</p>
  </div>
</section>

<section class="hanger hanger--back" aria-label="Back side: referral offer">
  <svg class="hanger__backdrop" viewBox="0 0 343 831" preserveAspectRatio="none" aria-hidden="true">
    <defs>
      <linearGradient id="poolBack" x1="0" y1="0" x2="0" y2="1">
        <stop offset="0" stop-color="#1f94dc"/>
        <stop offset="1" stop-color="#0f6cbf"/>
      </linearGradient>
    </defs>
    <path d="M0 150 C110 175 230 130 343 152 L343 831 L0 831 Z" fill="url(#poolBack)"/>
    <path d="M0 162 C110 186 230 142 343 164" fill="none" stroke="#ffffff" stroke-width="4" opacity="0.8"/>
    <path d="M0 700 C100 665 230 715 343 675 L343 831 L0 831 Z" fill="#ffffff"/>
  </svg>
  <div class="splash-art" style="left:14px;top:44px;width:104px;height:96px;" role="img" aria-label="Light blue water splash illustration"></div>
  <div class="wave-art" style="left:226px;top:14px;width:115px;height:132px;" role="img" aria-label="Blue ocean wave illustration"></div>
  <div class="hanger__hole"></div>

  <div class="referral">
    <p>CURRENT CUSTOMERS WILL GET</p>
    <p class="referral__amount">$10 OFF</p>
    <p>IF THEY REFER US TO A FRIEND AND</p>
    <p>SIGN UP FOR</p>
    <p class="referral__plan">"TERVIN PREMIUM POOL SERVICE"</p>
  </div>

  <div class="mascot-art" style="left:18px;top:376px;width:282px;height:190px;" role="img" aria-label="Cartoon shark mascot holding a pool skimmer net"></div>
  <p class="brand-name" style="left:20px;top:582px;width:300px;font-size:46px;line-height:56px;color:#ffffff;">Tervin Pools</p>
</section>

</body>
</html>
```